Brightvane Group Word Press Website

We need a graphical, fun website that conveys our messaging of providing the Top-Tier Keystone Outreach Program for Mortgage Loan Officers and Realtors. Our system uses AI and Predictive Analysis to uncover the 'Gold' hidden in contact databases. The 'Gold' is defined as people who are in the market or likely to be in the market soon. We place that 'Gold' in the form of Contact Name, Address, Phone and Email on a Daily To Do List detailing what type of contact should be made.

Target Market(s)

Mortgage Loan Officers and Realtors

Industry/Entity Type

Mortgage & Real Estate

Coding

Coded - Design and coding required

Number of Pages Required

5+ page

Requirements
Must have
• I like the look of this site- https://www.hearthloanstudio.example/
Nice to have
• Please create a flow that is similar to https://www.hearthloanstudio.example/, but better, more dynamic. Site must be responsive and mobile friendly. Site will have embedded videos. Site need to convey a message of hope, imagination, innovation, results oriented, better than the rest, victory!
Should not have
• Nothing cheesy or low class.

```html
<!DOCTYPE html>
<html lang="en">
<head>
<meta charset="utf-8">
<title>Brightvane Group — Presentation</title>
<link rel="stylesheet" href="https://fonts.googleapis.com/css2?family=Montserrat:wght@700;800;900&family=Poppins:wght@400;500;600;700&display=swap">
<style>
:root{
  --board:#000000;
  --gold:#e8b422;
  --gold-light:#f6d35c;
  --gold-deep:#c8921a;
  --blue:#0b6fe3;
  --blue-deep:#0657b8;
  --ink:#1c1c1c;
  --dark:#262626;
  --navy:#0c1a33;
  --navy-2:#13264a;
  --paper:#f4f4f4;
  --white:#ffffff;
  --muted:#8a8a8a;
}
*{box-sizing:border-box;margin:0;padding:0}
html,body{width:1200px;height:4087px;overflow:hidden;background:var(--board)}
body{position:relative;font-family:"Poppins",sans-serif;color:var(--white)}
.abs{position:absolute}
.board-title{font-family:"Montserrat",sans-serif;font-weight:800;color:var(--white);text-align:center;position:absolute}
.brand-mark{position:absolute;left:0;width:1200px;top:70px;display:flex;flex-direction:column;align-items:center;gap:22px}
.brand-mark .dot{width:70px;height:70px;border-radius:50%;background:var(--blue)}
.brand-mark .name{font-family:"Poppins",sans-serif;font-weight:700;font-size:52px;color:var(--gold);letter-spacing:1px}
.thanks{position:absolute;left:71px;top:3225px;font-family:"Montserrat",sans-serif;font-weight:900;font-size:104px;line-height:120px;letter-spacing:4px;color:var(--white)}

/* ---------- shared site pieces ---------- */
.site{position:absolute;background:var(--paper);overflow:hidden;color:var(--ink)}
.photo{position:absolute}
.btn{position:absolute;background:linear-gradient(180deg,var(--gold-light),var(--gold));color:var(--ink);font-weight:500;display:flex;align-items:center;justify-content:center}
.h-sec{position:absolute;font-weight:700;color:var(--ink);text-transform:uppercase}
.logo{position:absolute;display:flex;align-items:center;gap:4px}
.logo .sq{border-radius:50%;background:var(--blue)}
.logo .word{font-weight:700;color:var(--gold)}
.card{position:absolute;background:var(--white);box-shadow:0 1px 6px rgba(0,0,0,.12)}
.field-label{position:absolute;color:var(--ink)}
.field-ph{position:absolute;color:#a5a5a5}
.field-line{position:absolute;height:1px;background:#cfcfcf}
.arrow{position:absolute;border-radius:50%;display:flex;align-items:center;justify-content:center;color:var(--white);font-weight:700}

/* ---------- desktop ---------- */
.desk{left:119px;top:521px;width:587px;height:2153px}
.desk .nav a{position:absolute;top:8px;font-size:7px;color:var(--white)}
.desk .phone-pill{position:absolute;left:455px;top:0;width:132px;height:27px;background:var(--gold);color:var(--ink);font-size:7px;display:flex;align-items:center;justify-content:center;gap:5px}
.desk .hero-title{position:absolute;left:20px;width:280px;top:92px;text-align:center;font-weight:700;font-size:25px;line-height:34px;color:var(--white)}
.desk .hero-sub{position:absolute;left:20px;width:280px;top:170px;text-align:center;font-size:10px;line-height:17px;color:var(--white)}
.desk .small{font-size:5.6px;line-height:9px;color:#555}
.desk .svc{width:165px;height:108px;display:flex;flex-direction:column;align-items:center;padding-top:14px}
.desk .svc p{font-size:5.4px;line-height:8px;color:#666;text-align:center;margin-top:10px;width:120px}
.desk .feat{position:absolute;left:289px;display:flex;gap:14px}
.desk .feat .ic{width:38px;height:38px;border:1px solid #d9d9d9;display:flex;align-items:center;justify-content:center}
.desk .feat h4{font-size:7.5px;font-weight:500;color:var(--gold);margin-top:2px}
.desk .feat p{font-size:5.6px;line-height:9px;color:#e5e5e5;width:210px;margin-top:4px}
.desk .blog{width:165px;height:164px;background:var(--blue);box-shadow:0 1px 5px rgba(0,0,0,.15)}
.desk .blog .img{position:absolute;left:0;top:0;width:165px;height:100px}
.desk .blog .meta{position:absolute;left:10px;top:105px;font-size:5px;color:var(--white)}
.desk .blog .t{position:absolute;left:10px;top:116px;font-size:7.5px;line-height:11px;color:var(--white);width:130px}
.desk .blog .bar{position:absolute;left:10px;bottom:4px;width:110px;height:2px;background:var(--gold)}
.desk .blog .pin{position:absolute;left:10px;top:142px;width:8px;height:8px;border-radius:50%;background:var(--gold)}
.desk .foot h5{position:absolute;font-size:6.5px;font-weight:500;color:var(--white)}
.desk .foot p,.desk .foot li{font-size:5.4px;line-height:8.5px;color:#dcdcdc;list-style:none}

/* ---------- mobile ---------- */
.mob{left:846px;top:521px;width:244px;height:3566px}
.mob .foot-h{position:absolute;left:11px;font-size:15px;font-weight:500;color:var(--white)}
.mob .foot-p{position:absolute;left:11px;font-size:12px;line-height:22px;color:var(--white)}
.mob .svc-li{display:flex;align-items:center;gap:16px;font-size:12px;color:var(--white);height:28.5px}
.mob .svc-li i{width:7px;height:7px;border-radius:50%;background:var(--gold);display:block}
</style>
</head>
<body>

<div class="brand-mark" aria-label="Brightvane Group">
  <span class="dot"></span>
  <span class="name">Brightvane Group</span>
</div>

<h1 class="board-title" style="left:0;width:1200px;top:300px;font-size:72px;letter-spacing:2px">PRESENTATION</h1>
<h2 class="board-title" style="left:212px;width:400px;top:452px;font-size:33px">DESKTOP VIEW</h2>
<h2 class="board-title" style="left:822px;width:300px;top:452px;font-size:33px">MOBILE VIEW</h2>

<!-- ================= DESKTOP ================= -->
<section class="site desk" aria-label="Desktop page layout">
  <!-- hero -->
  <div class="photo" role="img" aria-label="Photo of a smiling loan officer talking with a client in a bright office" style="left:0;top:0;width:587px;height:305px;background:linear-gradient(90deg,#1a1410 0%,#3a2c22 35%,#7a6452 65%,#a89580 100%)"></div>
  <div class="logo" style="left:36px;top:12px"><span class="sq" style="width:9px;height:9px"></span><span class="word" style="font-size:8px">Brightvane Group</span></div>
  <nav class="nav">
    <a style="left:226px;color:var(--gold)">Home</a>
    <a style="left:271px">Services</a>
    <a style="left:326px">About</a>
    <a style="left:371px">Blog</a>
    <a style="left:410px">Contact</a>
  </nav>
  <div class="phone-pill">
    <svg width="9" height="9" viewBox="0 0 24 24"><circle cx="12" cy="12" r="11" fill="none" stroke="#1c1c1c" stroke-width="2"/><path d="M8 6l2 3-1.5 1.5c.8 1.8 2.2 3.2 4 4L14 13l3 2-1 2.5c-5 0-9-4-9-9z" fill="#1c1c1c"/></svg>
    (555) 304-7712
  </div>
  <h2 class="hero-title">Mortgage Is<br>A Great For You</h2>
  <p class="hero-sub">The Top-Tier Keystone Outreach Program<br>System</p>
  <div class="btn" style="left:114px;top:212px;width:92px;height:16px;font-size:6px">Schedule Consultation</div>
  <svg class="abs" style="left:0;top:190px" width="587" height="116" viewBox="0 0 587 116">
    <path d="M0 10 Q250 150 587 72 L587 116 L0 116 Z" fill="#f4f4f4"/>
    <path d="M0 10 Q250 150 587 72" fill="none" stroke="#e8b422" stroke-width="7"/>
  </svg>

  <!-- about -->
  <div class="photo" role="img" aria-label="Collage of round team photos arranged around a star shape" style="left:40px;top:317px;width:230px;height:178px;border-radius:50%;background:radial-gradient(circle,#d9d2c8 0%,#8da3bd 55%,#f4f4f4 72%)"></div>
  <h3 class="h-sec" style="left:338px;top:352px;font-size:11px">About Us</h3>
  <p class="abs small" style="left:338px;top:372px;width:215px">It is a long established fact that a reader will be distracted by the readable content of a page when looking at its layout. The point of using Lorem Ipsum is that it has a more-or-less normal distribution of letters, as<br><br>It took like readable English. Many desktop publishing packages and web page editors now use Lorem Ipsum as their default model text, and a search for lorem ipsum will uncover many web sites still in their infancy. Various versions have evolved over the years, sometimes by accident, sometimes.</p>
  <div class="btn" style="left:338px;top:487px;width:68px;height:19px;font-size:6px">Learn More</div>
  <svg class="abs" style="left:0;top:480px" width="587" height="130" viewBox="0 0 587 130"><path d="M587 0 Q420 60 250 130 L587 130 Z" fill="#ececec"/></svg>

  <!-- services -->
  <h3 class="h-sec" style="left:0;width:587px;text-align:center;top:616px;font-size:12px">Our Gold Servicess</h3>
  <div class="card svc" style="left:33px;top:651px"><svg width="36" height="30" viewBox="0 0 36 30"><rect x="3" y="2" width="30" height="19" fill="none" stroke="#0b6fe3" stroke-width="1.6"/><path d="M14 21v5h8v-5M10 27h16M9 15l6-6 4 4 7-7" fill="none" stroke="#0b6fe3" stroke-width="1.6"/></svg><p>Lorem Ipsum has been the industry's standard dummy text ever since the 1500s .</p></div>
  <div class="card svc" style="left:210px;top:651px"><svg width="36" height="30" viewBox="0 0 36 30"><path d="M12 4h12l-3 6h-6zM10 12h16c4 5 5 16-8 16S6 17 10 12z" fill="none" stroke="#0b6fe3" stroke-width="1.6"/><circle cx="18" cy="20" r="3" fill="none" stroke="#0b6fe3" stroke-width="1.4"/></svg><p>Lorem Ipsum has been the industry's standard dummy text ever since the 1500s .</p></div>
  <div class="card svc" style="left:386px;top:651px"><svg width="36" height="30" viewBox="0 0 36 30"><rect x="5" y="3" width="26" height="24" fill="none" stroke="#0b6fe3" stroke-width="1.6"/><path d="M9 9h18M9 14h10M9 19h18M9 23h12" stroke="#0b6fe3" stroke-width="1.4"/></svg><p>Lorem Ipsum has been the industry's standard dummy text ever since the 1500s .</p></div>
  <div class="card svc" style="left:33px;top:770px"><svg width="36" height="30" viewBox="0 0 36 30"><rect x="8" y="2" width="20" height="26" fill="none" stroke="#0b6fe3" stroke-width="1.6"/><path d="M12 8h12M12 13h12M12 18h8" stroke="#0b6fe3" stroke-width="1.4"/></svg><p>Lorem Ipsum has been the industry's standard dummy text ever since the 1500s .</p></div>
  <div class="card svc" style="left:210px;top:770px"><svg width="36" height="30" viewBox="0 0 36 30"><path d="M2 14l8-8 8 6 8-6 8 8-16 12z" fill="none" stroke="#0b6fe3" stroke-width="1.6"/></svg><p>Lorem Ipsum has been the industry's standard dummy text ever since the 1500s .</p></div>
  <div class="card svc" style="left:386px;top:770px"><svg width="36" height="30" viewBox="0 0 36 30"><circle cx="18" cy="13" r="8" fill="none" stroke="#0b6fe3" stroke-width="1.6"/><path d="M15 22h6v5h-6zM18 1v2M6 13H4M32 13h-2" stroke="#0b6fe3" stroke-width="1.6" fill="none"/></svg><p>Lorem Ipsum has been the industry's standard dummy text ever since the 1500s .</p></div>
  <div class="btn" style="left:257px;top:881px;width:71px;height:19px;font-size:6px">View All</div>

  <!-- features -->
  <div class="abs" style="left:0;top:933px;width:587px;height:340px;background:var(--dark)"></div>
  <div class="photo" role="img" aria-label="Collage of round photos of business people arranged around a star shape" style="left:32px;top:979px;width:238px;height:246px;border-radius:50%;background:radial-gradient(circle,#e9e9e9 0%,#6b6b6b 50%,#262626 72%)"></div>
  <h3 class="h-sec" style="left:286px;top:967px;font-size:11px;color:var(--white)">Our Gold Features</h3>
  <div class="feat" style="top:1012px"><div class="ic"><svg width="20" height="20" viewBox="0 0 24 24"><path d="M12 3l2.4 5 5.6.8-4 3.9 1 5.5-5-2.6-5 2.6 1-5.5-4-3.9 5.6-.8z" fill="none" stroke="#fff" stroke-width="1.3"/></svg></div><div><h4>5 Star Ratings</h4><p>There are many variations of passages of Lorem Ipsum available, but the majority have suffered alteration</p></div></div>
  <div class="feat" style="top:1063px"><div class="ic"><svg width="20" height="20" viewBox="0 0 24 24"><circle cx="12" cy="12" r="8" fill="none" stroke="#fff" stroke-width="1.3"/><path d="M8 12l3 3 5-6" fill="none" stroke="#fff" stroke-width="1.3"/></svg></div><div><h4>Completed Projects</h4><p>There are many variations of passages of Lorem Ipsum available, but the majority have suffered alteration</p></div></div>
  <div class="feat" style="top:1114px"><div class="ic"><svg width="20" height="20" viewBox="0 0 24 24"><circle cx="12" cy="8" r="3.5" fill="none" stroke="#fff" stroke-width="1.3"/><path d="M5 20c1-5 13-5 14 0" fill="none" stroke="#fff" stroke-width="1.3"/></svg></div><div><h4>Happy Clients</h4><p>There are many variations of passages of Lorem Ipsum available, but the majority have suffered alteration</p></div></div>
  <div class="feat" style="top:1165px"><div class="ic"><svg width="20" height="20" viewBox="0 0 24 24"><circle cx="8" cy="8" r="3" fill="none" stroke="#fff" stroke-width="1.3"/><circle cx="16" cy="8" r="3" fill="none" stroke="#fff" stroke-width="1.3"/><path d="M2 19c1-4 11-4 12 0M10 19c1-4 11-4 12 0" fill="none" stroke="#fff" stroke-width="1.3"/></svg></div><div><h4>Team Member</h4><p>There are many variations of passages of Lorem Ipsum available,but the majority have suffered alteration</p></div></div>
  <svg class="abs" style="left:0;top:1160px" width="587" height="114" viewBox="0 0 587 114">
    <path d="M120 114 Q300 20 587 95 L587 114 Z" fill="#f4f4f4"/>
    <path d="M120 114 Q300 20 587 95" fill="none" stroke="#e8b422" stroke-width="8"/>
  </svg>

  <!-- blog -->
  <h3 class="h-sec" style="left:0;width:587px;text-align:center;top:1303px;font-size:12px">Recent Blog</h3>
  <article class="abs blog" style="left:33px;top:1335px"><div class="img" role="img" aria-label="Photo of two professionals shaking hands" style="background:linear-gradient(135deg,#e6e6e6,#9aa6b4)"></div><span class="meta">MAR 16,2022 / BY LOREM IPSUM</span><p class="t">Lorem Ipsum is simply dummy text of the printing</p><span class="pin"></span><span class="bar"></span></article>
  <article class="abs blog" style="left:210px;top:1335px"><div class="img" role="img" aria-label="Photo of a team meeting around a table" style="background:linear-gradient(135deg,#5b4636,#c9b49c)"></div><span class="meta">MAR 16,2022 / BY LOREM IPSUM</span><p class="t">Lorem Ipsum is simply dummy text of the printing</p><span class="pin"></span><span class="bar"></span></article>
  <article class="abs blog" style="left:386px;top:1335px"><div class="img" role="img" aria-label="Photo of hands typing on a laptop" style="background:linear-gradient(135deg,#3a3a3a,#9a8a7c)"></div><span class="meta">MAR 16,2022 / BY LOREM IPSUM</span><p class="t">Lorem Ipsum is simply dummy text of the printing</p><span class="pin"></span><span class="bar"></span></article>
  <div class="btn" style="left:257px;top:1513px;width:71px;height:19px;font-size:6px">View All</div>

  <!-- contact -->
  <div class="abs" style="left:349px;top:1598px;width:203px;height:198px;background:var(--blue)"></div>
  <div class="photo" role="img" aria-label="Photo of a smiling agent in a suit offering a handshake" style="left:35px;top:1603px;width:205px;height:214px;background:linear-gradient(135deg,#e8e8e8,#8a8f98 60%,#2a2f3a);box-shadow:0 1px 6px rgba(0,0,0,.2)"></div>
  <div class="card" style="left:190px;top:1622px;width:350px;height:210px"></div>
  <h3 class="h-sec" style="left:220px;top:1650px;font-size:12px">Contact An Agent</h3>
  <span class="field-label" style="left:220px;top:1693px;font-size:6px">Your Name</span>
  <span class="field-ph" style="left:220px;top:1702px;font-size:5px">Alex Rowan</span>
  <span class="field-line" style="left:220px;top:1712px;width:135px"></span>
  <span class="field-label" style="left:375px;top:1693px;font-size:6px">Email</span>
  <span class="field-ph" style="left:375px;top:1702px;font-size:5px">alexrowan@mail.example</span>
  <span class="field-line" style="left:375px;top:1712px;width:135px"></span>
  <span class="field-label" style="left:220px;top:1733px;font-size:6px">Message</span>
  <span class="field-ph" style="left:220px;top:1743px;font-size:5px">Hi,Do you have a moment to talk Us !</span>
  <span class="field-line" style="left:220px;top:1755px;width:290px"></span>
  <div class="btn" style="left:220px;top:1774px;width:73px;height:21px;font-size:6px">Submit Now</div>

  <!-- footer -->
  <svg class="abs" style="left:0;top:1868px" width="587" height="285" viewBox="0 0 587 285">
    <defs><linearGradient id="navyDesk" x1="0" y1="0" x2="0" y2="1"><stop offset="0" stop-color="#13264a"/><stop offset="1" stop-color="#0a1730"/></linearGradient></defs>
    <path d="M0 80 Q280 -40 587 70 L587 285 L0 285 Z" fill="url(#navyDesk)"/>
    <path d="M0 80 Q280 -40 587 70" fill="none" stroke="#e8b422" stroke-width="9"/>
  </svg>
  <div class="logo" style="left:0;width:587px;justify-content:center;top:1918px"><span class="sq" style="width:10px;height:10px"></span><span class="word" style="font-size:10px">Brightvane Group</span></div>
  <div class="foot">
    <h5 style="left:35px;top:2000px">ABOUT</h5>
    <p class="abs" style="left:35px;top:2014px;width:135px">It is a long established fact that a reader will be distracted by the readable content of a page when looking at its layout.The point of using Lorem</p>
    <div class="abs" style="left:35px;top:2056px;display:flex;gap:4px"><span style="width:14px;height:14px;border-radius:50%;background:var(--gold)"></span><span style="width:14px;height:14px;border-radius:50%;background:var(--gold)"></span><span style="width:14px;height:14px;border-radius:50%;background:var(--gold)"></span><span style="width:14px;height:14px;border-radius:50%;background:var(--gold)"></span></div>
    <h5 style="left:188px;top:2000px">CONTACT</h5>
    <p class="abs" style="left:202px;top:2014px;width:95px">Marlowe Quay 2207 BK Alder Bay, Oregon</p>
    <p class="abs" style="left:202px;top:2043px;color:var(--gold)">555-218-0463</p>
    <p class="abs" style="left:202px;top:2063px">hello@brightvane.example</p>
    <svg class="abs" style="left:190px;top:2015px" width="7" height="60" viewBox="0 0 7 60"><circle cx="3.5" cy="3" r="2.5" fill="#fff"/><circle cx="3.5" cy="31" r="2.5" fill="#fff"/><rect x="0.5" y="49" width="6" height="4" fill="#fff"/></svg>
    <h5 style="left:316px;top:2000px">SERVICE</h5>
    <ul class="abs" style="left:330px;top:2014px"><li>low-code services</li><li>Serverless mode</li><li>ETL/integration</li><li>Script runtime code</li><li>Cloud task runners</li></ul>
    <h5 style="left:419px;top:2000px">NEWSLETTER</h5>
    <p class="abs" style="left:419px;top:2014px;width:135px">he point of using Lorem Ipsum is that it has a more-or-less normal distribution</p>
    <div class="abs" style="left:419px;top:2035px;width:135px;height:17px;background:var(--white);color:#777;font-size:5px;display:flex;align-items:center;padding-left:6px">Enter Your Mail ID</div>
    <div class="btn" style="left:419px;top:2058px;width:72px;height:15px;font-size:5.5px">Subscribe Now</div>
    <div class="abs" style="left:35px;top:2102px;width:517px;height:1px;background:#3a4a68"></div>
    <p class="abs" style="left:0;width:587px;text-align:center;top:2112px">© 2021 <span style="color:var(--gold)">BRIGHTVANE GROUP</span>. All rights reserved.</p>
  </div>
</section>

<!-- ================= MOBILE ================= -->
<section class="site mob" aria-label="Mobile page layout">
  <div class="photo" role="img" aria-label="Photo of a smiling loan officer talking with a client in a bright office" style="left:0;top:0;width:244px;height:217px;background:linear-gradient(90deg,#1a1410 0%,#3a2c22 45%,#8a7462 80%,#b3a08a 100%)"></div>
  <div class="logo" style="left:9px;top:10px"><span class="sq" style="width:8px;height:8px"></span><span class="word" style="font-size:7.5px">Brightvane Group</span></div>
  <svg class="abs" style="left:210px;top:10px" width="22" height="16" viewBox="0 0 22 16"><path d="M0 1.5h22M0 8h22M0 14.5h22" stroke="#fff" stroke-width="2.5"/></svg>
  <h2 class="abs" style="left:9px;top:64px;font-size:15px;line-height:25px;font-weight:700;color:var(--white)">Mortgage Is<br>A Great For You</h2>
  <p class="abs" style="left:9px;top:118px;font-size:9.5px;line-height:16px;color:var(--white);width:190px">The Top-Tier Keystone Outreach Program</p>
  <div class="btn" style="left:11px;top:165px;width:141px;height:21px;font-size:10px">Schedule Consultation</div>
  <svg class="abs" style="left:0;top:170px" width="244" height="50" viewBox="0 0 244 50">
    <path d="M0 4 Q120 70 244 22 L244 50 L0 50 Z" fill="#f4f4f4"/>
    <path d="M0 4 Q120 70 244 22" fill="none" stroke="#e8b422" stroke-width="5"/>
  </svg>

  <div class="photo" role="img" aria-label="Collage of round team photos arranged around a star shape" style="left:43px;top:233px;width:159px;height:151px;border-radius:50%;background:radial-gradient(circle,#d9d2c8 0%,#8da3bd 55%,#f4f4f4 72%)"></div>
  <h3 class="h-sec" style="left:11px;top:414px;font-size:15px">About Us</h3>
  <p class="abs" style="left:11px;top:440px;width:222px;font-size:10px;line-height:19.5px;color:#555">It is a long established fact that a reader will be distracted by the readable content of a page when looking at its layout. The point of using Lorem Ipsum is that it has a more-or-less normal distribution of letters, as opposed to using 'Content here, content here', making .</p>
  <div class="btn" style="left:11px;top:594px;width:141px;height:27px;font-size:11px">Learn More</div>

  <h3 class="h-sec" style="left:0;width:244px;text-align:center;top:740px;font-size:15px">Our Gold Services</h3>
  <div class="card" style="left:17px;top:776px;width:210px;height:164px;display:flex;flex-direction:column;align-items:center;padding-top:24px">
    <svg width="54" height="46" viewBox="0 0 36 30"><rect x="3" y="2" width="30" height="19" fill="none" stroke="#0b6fe3" stroke-width="1.4"/><path d="M14 21v5h8v-5M10 27h16M9 15l6-6 4 4 7-7" fill="none" stroke="#0b6fe3" stroke-width="1.4"/></svg>
    <p style="font-size:10px;line-height:17px;color:#777;text-align:center;width:190px;margin-top:18px">Lorem Ipsum has been the industry's standard dummy text ever since the 1500s .</p>
  </div>
  <span class="arrow" style="left:94px;top:950px;width:26px;height:26px;background:#555;font-size:13px">‹</span>
  <span class="arrow" style="left:125px;top:950px;width:26px;height:26px;background:var(--gold);font-size:13px">›</span>

  <div class="abs" style="left:0;top:1008px;width:244px;height:472px;background:var(--dark)"></div>
  <h3 class="h-sec" style="left:0;width:244px;text-align:center;top:1045px;font-size:15px;color:var(--white)">Our Gold Features</h3>
  <div class="abs" style="left:11px;top:1098px;width:51px;height:51px;border:1px solid #d9d9d9;display:flex;align-items:center;justify-content:center"><svg width="30" height="30" viewBox="0 0 24 24"><path d="M12 3l2.4 5 5.6.8-4 3.9 1 5.5-5-2.6-5 2.6 1-5.5-4-3.9 5.6-.8z" fill="none" stroke="#fff" stroke-width="1.1"/></svg></div>
  <h4 class="abs" style="left:75px;top:1094px;font-size:14px;font-weight:500;color:var(--gold)">5 Star Ratings</h4>
  <p class="abs" style="left:75px;top:1118px;width:160px;font-size:11px;line-height:16.5px;color:var(--white)">There are many variations of passages of Lorem Ipsum available, but the majority .</p>
  <div class="abs" style="left:11px;top:1211px;width:51px;height:51px;border:1px solid #d9d9d9;display:flex;align-items:center;justify-content:center"><svg width="30" height="30" viewBox="0 0 24 24"><circle cx="12" cy="12" r="8" fill="none" stroke="#fff" stroke-width="1.1"/><path d="M8 12l3 3 5-6" fill="none" stroke="#fff" stroke-width="1.1"/></svg></div>
  <h4 class="abs" style="left:75px;top:1207px;font-size:14px;font-weight:500;color:var(--gold)">Completed Projects</h4>
  <p class="abs" style="left:75px;top:1231px;width:160px;font-size:11px;line-height:16.5px;color:var(--white)">There are many variations of passages of Lorem Ipsum available, but the majority .</p>
  <span class="arrow" style="left:168px;top:1318px;width:24px;height:24px;background:#555;font-size:12px">‹</span>
  <span class="arrow" style="left:199px;top:1318px;width:24px;height:24px;background:var(--gold);font-size:12px">›</span>
  <div class="photo" role="img" aria-label="Collage of round photos of business people arranged around a star shape" style="left:0;top:1306px;width:146px;height:159px;border-radius:50%;background:radial-gradient(circle,#e9e9e9 0%,#6b6b6b 50%,#262626 72%)"></div>
  <svg class="abs" style="left:0;top:1420px" width="244" height="62" viewBox="0 0 244 62">
    <path d="M40 62 Q130 0 244 50 L244 62 Z" fill="#f4f4f4"/>
    <path d="M40 62 Q130 0 244 50" fill="none" stroke="#e8b422" stroke-width="6"/>
  </svg>

  <h3 class="h-sec" style="left:0;width:244px;text-align:center;top:1507px;font-size:15px">Recent Blog</h3>
  <article class="abs" style="left:11px;top:1546px;width:222px;height:219px;background:var(--blue);box-shadow:0 1px 5px rgba(0,0,0,.15)">
    <div class="photo" role="img" aria-label="Photo of two professionals shaking hands" style="left:0;top:0;width:222px;height:128px;background:linear-gradient(135deg,#e6e6e6,#9aa6b4)"></div>
    <span class="abs" style="left:12px;top:136px;font-size:7.5px;color:var(--white)">MAR 16,2022 / BY LOREM IPSUM</span>
    <p class="abs" style="left:12px;top:152px;width:180px;font-size:10.5px;line-height:16px;color:var(--white)">Lorem Ipsum is simply dummy text of the printing</p>
    <span class="abs" style="left:12px;top:192px;width:11px;height:11px;border-radius:50%;background:var(--gold)"></span>
    <span class="abs" style="left:12px;bottom:5px;width:150px;height:2px;background:var(--gold)"></span>
  </article>
  <span class="arrow" style="left:3px;top:1620px;width:26px;height:26px;background:#555;font-size:13px">‹</span>
  <span class="arrow" style="left:217px;top:1620px;width:26px;height:26px;background:var(--gold);font-size:13px">›</span>
  <div class="btn" style="left:60px;top:1780px;width:124px;height:28px;font-size:11px">View All</div>

  <div class="card" style="left:11px;top:1844px;width:222px;height:468px"></div>
  <div class="photo" role="img" aria-label="Photo of a smiling agent in a suit offering a handshake" style="left:17px;top:1849px;width:210px;height:201px;background:linear-gradient(135deg,#e8e8e8,#8a8f98 60%,#2a2f3a)"></div>
  <h3 class="h-sec" style="left:20px;top:2068px;font-size:16px;line-height:22px">Contact An<br>Agent</h3>
  <span class="field-label" style="left:20px;top:2130px;font-size:8.5px">Your Name</span>
  <span class="field-ph" style="left:20px;top:2144px;font-size:8px">Alex Rowan</span>
  <span class="field-line" style="left:20px;top:2160px;width:205px"></span>
  <span class="field-label" style="left:20px;top:2175px;font-size:8.5px">Email</span>
  <span class="field-ph" style="left:20px;top:2188px;font-size:8px">alexrowan@mail.example</span>
  <span class="field-line" style="left:20px;top:2204px;width:205px"></span>
  <span class="field-label" style="left:20px;top:2217px;font-size:8.5px">Message</span>
  <span class="field-ph" style="left:20px;top:2231px;font-size:8px">Hi,Do you have a moment to talk Us !</span>
  <span class="field-line" style="left:20px;top:2247px;width:205px"></span>
  <div class="btn" style="left:24px;top:2262px;width:122px;height:28px;font-size:11px">Submit Now</div>

  <svg class="abs" style="left:0;top:2370px" width="244" height="1196" viewBox="0 0 244 1196">
    <defs><linearGradient id="navyMob" x1="0" y1="0" x2="0" y2="1"><stop offset="0" stop-color="#13264a"/><stop offset="1" stop-color="#0a1730"/></linearGradient></defs>
    <path d="M0 40 Q120 -10 244 30 L244 1196 L0 1196 Z" fill="url(#navyMob)"/>
    <path d="M0 40 Q120 -10 244 30" fill="none" stroke="#e8b422" stroke-width="7"/>
  </svg>
  <div class="logo" style="left:14px;top:2480px"><span class="sq" style="width:14px;height:14px"></span><span class="word" style="font-size:13px">Brightvane Group</span></div>
  <h5 class="foot-h" style="top:2580px">ABOUT</h5>
  <p class="foot-p" style="top:2625px;width:225px;font-size:12px">It is a long established fact that a reader will be distracted by the readable content of a page when looking at its layout.The point of using Lorem</p>
  <div class="abs" style="left:11px;top:2770px;width:30px;height:1px;background:#5a6a88"></div>
  <h5 class="foot-h" style="top:2802px">CONTACT</h5>
  <svg class="abs" style="left:11px;top:2852px" width="14" height="135" viewBox="0 0 14 135"><path d="M7 1a5 5 0 0 0-5 5c0 4 5 10 5 10s5-6 5-10a5 5 0 0 0-5-5z" fill="#fff"/><path d="M2 75l3-1 2 3-1.5 1.5c1 2 2 3 4 4L11 81l3 2-1 2.5C7 85 2 80 2 75z" fill="#fff"/><rect x="1" y="114" width="12" height="8" fill="#fff"/></svg>
  <p class="foot-p" style="left:42px;top:2848px;width:195px;line-height:20px">Marlowe Quay 2207 BK Alder Bay, Oregon</p>
  <p class="foot-p" style="left:42px;top:2925px;color:var(--gold)">555-218-0463</p>
  <p class="foot-p" style="left:42px;top:2963px">hello@brightvane.example</p>
  <div class="abs" style="left:11px;top:3020px;width:50px;height:1px;background:#5a6a88"></div>
  <h5 class="foot-h" style="top:3040px">SERVICE</h5>
  <ul class="abs" style="left:11px;top:3080px;list-style:none">
    <li class="svc-li"><i></i>low-code services</li>
    <li class="svc-li"><i></i>Serverless mode</li>
    <li class="svc-li"><i></i>ETL/integration</li>
    <li class="svc-li"><i></i>Script runtime code</li>
    <li class="svc-li"><i></i>Cloud task runners.</li>
  </ul>
  <div class="abs" style="left:11px;top:3252px;width:50px;height:1px;background:#5a6a88"></div>
  <h5 class="foot-h" style="top:3278px">NEWSLETTER</h5>
  <p class="foot-p" style="top:3320px;width:225px;font-size:12px">he point of using Lorem Ipsum is that it has a more-or-less normal distribution letters,</p>
  <div class="abs" style="left:11px;top:3418px;width:222px;height:38px;background:var(--white);color:#555;font-size:12px;display:flex;align-items:center;padding-left:16px">Enter Your Mail ID</div>
  <div class="btn" style="left:11px;top:3463px;width:124px;height:26px;font-size:11px">Subscribe Now</div>
  <p class="abs" style="left:11px;top:3515px;font-size:9.5px;color:var(--white)">© 2021 <span style="color:var(--gold)">BRIGHTVANE GROUP</span>. All rights reserved.</p>
</section>

<p class="thanks">THANKS<br>FOR<br>WATCHING</p>

</body>
</html>
```